Hi,

I would like to create a beer label for our new beer we are creating,

We are called "The Larkmoor Brewing Co."

Our new beer is called "The Brass Lantern" which is a "Pale Ale" with an "ABV 4.8%"

our tag line is "Built For Sessionability"

Everything writen in inverted comma's I would like on the label

I would like it to be a round beer label as well with some sort of picture in the background.

This is our first design of any kind for the company so we do not have a logo or any designs so its open to anything. I would like it to be new and trendy with an older style feel to it.

Industry/Entity Type

Graphic Design

Requirements
Must have
• Round so I can convert into a beer coaster,
needs to have alcohol percentage.

```html
<!DOCTYPE html>
<html lang="en">
<head>
<meta charset="utf-8">
<title>The Brass Lantern – Pale Ale Label</title>
<link href="https://fonts.googleapis.com/css2?family=Lobster&family=Libre+Baskerville&display=swap" rel="stylesheet">
<style>
  :root {
    --page-bg: #eeeeee;
    --rim-gold-light: #f6e2a6;
    --rim-gold-dark: #b88a2e;
    --ring-navy: #133a84;
    --ring-blue: #2a5fb8;
    --field-sky: #1ea7e6;
    --field-sky-light: #46bdf0;
    --snow: #f4f8fb;
    --snow-shade: #9fc4dc;
    --title-gold: #f3c572;
    --title-edge: #6e1f12;
    --brand-green: #2f6b2c;
    --tagline-red: #8a2b14;
    --abv-ink: #ffffff;
  }
  html, body {
    margin: 0;
    width: 1200px;
    height: 1000px;
    overflow: hidden;
    background: var(--page-bg);
  }
  .canvas {
    position: relative;
    width: 1200px;
    height: 1000px;
  }
  .label-art {
    position: absolute;
    left: 0;
    top: 0;
  }
  .label-text {
    position: absolute;
    inset: 0;
    font-family: "Lobster", cursive;
  }
  .brand-name {
    position: absolute;
    left: 0;
    right: 0;
    top: 178px;
    text-align: center;
    font-size: 34px;
    color: var(--brand-green);
  }
  .beer-title {
    position: absolute;
    left: 0;
    right: 0;
    margin: 0;
    text-align: center;
    font-weight: 400;
    color: var(--title-gold);
    text-shadow: 2px 2px 0 var(--title-edge), 4px 5px 0 var(--title-edge);
    line-height: 1;
    transform: rotate(-4deg);
  }
  .beer-title .line-one {
    position: absolute;
    left: 0;
    right: 0;
    top: 250px;
    font-size: 128px;
  }
  .beer-title .line-two {
    position: absolute;
    left: 0;
    right: 0;
    top: 372px;
    font-size: 128px;
  }
  .beer-style {
    position: absolute;
    left: 640px;
    top: 480px;
    font-size: 62px;
    color: var(--title-gold);
    text-shadow: 2px 2px 0 var(--title-edge), 3px 4px 0 var(--title-edge);
    transform: rotate(-4deg);
  }
  .tagline {
    position: absolute;
    left: 0;
    right: 0;
    top: 640px;
    text-align: center;
    font-size: 44px;
    color: var(--tagline-red);
    transform: rotate(-8deg);
  }
  .abv {
    position: absolute;
    left: 0;
    right: 0;
    top: 738px;
    text-align: center;
    font-family: "Libre Baskerville", serif;
    font-size: 26px;
    color: var(--abv-ink);
  }
</style>
</head>
<body>
<main class="canvas">
  <svg class="label-art" width="1200" height="1000" viewBox="0 0 1200 1000">
    <defs>
      <linearGradient id="rim-gold" x1="0" y1="0" x2="1" y2="1">
        <stop offset="0" stop-color="var(--rim-gold-dark)"/>
        <stop offset="0.3" stop-color="var(--rim-gold-light)"/>
        <stop offset="0.6" stop-color="var(--rim-gold-dark)"/>
        <stop offset="1" stop-color="var(--rim-gold-light)"/>
      </linearGradient>
      <radialGradient id="ring-fill" cx="0.5" cy="0.5" r="0.5">
        <stop offset="0.75" stop-color="var(--ring-blue)"/>
        <stop offset="1" stop-color="var(--ring-navy)"/>
      </radialGradient>
      <radialGradient id="field-fill" cx="0.5" cy="0.35" r="0.6">
        <stop offset="0" stop-color="var(--field-sky-light)"/>
        <stop offset="1" stop-color="var(--field-sky)"/>
      </radialGradient>
      <linearGradient id="mountain-fill" x1="0" y1="0" x2="0" y2="1">
        <stop offset="0" stop-color="var(--snow-shade)"/>
        <stop offset="0.45" stop-color="var(--snow)"/>
        <stop offset="1" stop-color="var(--snow)"/>
      </linearGradient>
      <clipPath id="field-clip">
        <circle cx="600" cy="500" r="335"/>
      </clipPath>
    </defs>

    <circle class="label-rim" cx="600" cy="500" r="450" fill="url(#rim-gold)"/>
    <circle class="label-ring" cx="600" cy="500" r="438" fill="url(#ring-fill)"
            role="img" aria-label="Deep blue ring with halftone texture and water bubbles"/>
    <circle class="field-rim" cx="600" cy="500" r="343" fill="url(#rim-gold)"/>
    <circle class="label-field" cx="600" cy="500" r="335" fill="url(#field-fill)"/>

    <g clip-path="url(#field-clip)">
      <rect class="mountain-scene" x="250" y="540" width="700" height="130" fill="url(#mountain-fill)"
            role="img" aria-label="Snow-capped mountain range"/>
      <rect x="250" y="670" width="700" height="180" fill="var(--field-sky)"/>
    </g>
  </svg>

  <div class="label-text">
    <div class="brand-name">The Larkmoor Brewing Co.</div>
    <h1 class="beer-title">
      <span class="line-one">The Brass</span>
      <span class="line-two">Lantern</span>
    </h1>
    <div class="beer-style">Pale Ale</div>
    <div class="tagline">Built For Sessionability</div>
    <div class="abv">ABV 4.8%</div>
  </div>
</main>
</body>
</html>
```